Home page web design for a lawn specialist business

-The design must be based around the attached HPID (home page information design) called Turf Haven HPID. I've attached Word and PDF versions - these are the same. The table boxes are just for approximate placement of information and you can use boxes and bold shapes for this design.

All fonts used in the HPID are only examples - you can use any Google font you wish.

- Text that is in orange is for your information only. Text to go on the design is black. Some instructions are in the HPID. Please be creative!

-The design needs to be modern and exciting - colours are to be the green of the logo, and white ...and then choose dark green, or dark grey or black.

Logo - attached (it's not great quality but don't worry, we'll replace it later)

- I've provided the images for the galleries - they are labelled and will match the name in the HPID. Please use the supplied images!

- Examples of some websites that have great design... don't copy them please but they are similar in look to what we are after....
www.kelbrinworks.co.nz
http://www.rimsafe-guarding.co.nz/
http://www.brightnest.wb.gs/

Important: Width of content will be 1280 pixels when implemented as a web page but the winning design will need to supplied be on a 2000 pixel wide background so nav bars and background can extend outside the 1280 width.
Header height (without nav bar) 150-160 pixels.

We don't comment on individual designs but will choose a winning design promptly.

Industry/Entity Type

Business

Number of Pages Required

1 page

Font styles to use
Sans Serif

Requirements
Must have
• clean, modern, well-spaced design

```html
<!DOCTYPE html>
<html lang="en">
<head>
<meta charset="utf-8">
<title>Turf Haven – Lawn specialists</title>
<link rel="stylesheet" href="https://fonts.googleapis.com/css2?family=Raleway:wght@500;600;700&family=Open+Sans:wght@400;600&family=Roboto:wght@300;400&display=swap">
<style>
:root{
  --green:#3e9e2f;
  --green-bright:#4cb83a;
  --green-dark:#2f7d22;
  --green-text:#3a9a2a;
  --grey-dark:#3d3d3d;
  --grey-btn:#4a4a4a;
  --grey-text:#8a8a8a;
  --body-text:#444;
  --light:#f1f1f1;
  --white:#fff;
}
*{box-sizing:border-box;margin:0;padding:0}
html,body{width:1200px;height:3051px;overflow:hidden;background:var(--white)}
body{font-family:"Open Sans",Arial,sans-serif;color:var(--body-text);position:relative}
.abs{position:absolute}

/* header */
.site-header{position:absolute;left:0;top:0;width:1200px;height:146px}
.brand{position:absolute;left:92px;top:40px;display:flex;align-items:center;gap:14px}
.brand-square{width:48px;height:48px;background:var(--green)}
.brand-name{font-family:"Open Sans",sans-serif;font-weight:600;font-size:38px;color:var(--green)}
.header-info{position:absolute;right:88px;top:28px;text-align:right;font-size:12px;line-height:22px;color:#555}
.header-info .tag{font-family:"Raleway",sans-serif;font-weight:700;font-size:21px;color:var(--green-text);line-height:30px;margin-bottom:2px}

/* nav */
.main-nav{position:absolute;left:0;top:146px;width:1200px;height:70px;
  background:linear-gradient(#5cc24a,#3a9a2c);border-top:1px solid #78d266}
.main-nav ul{list-style:none;display:flex;margin-left:87px;height:100%}
.main-nav li{display:flex;align-items:center;padding:0 17px;font-size:12.5px;color:var(--white);text-transform:uppercase;font-weight:400}
.main-nav li.active{background:var(--grey-dark);padding:0 24px}

/* hero */
.hero{position:absolute;left:0;top:216px;width:1200px;height:549px;
  background:linear-gradient(112deg,#8a8782 0%,#6d5d50 25%,#5e4d40 44%,#4f9a2c 46%,#4aa034 70%,#6cb548 100%)}
.hero-caption{position:absolute;color:var(--white);font-family:"Roboto",sans-serif;font-weight:300;line-height:1.05}
.hero-caption .big{font-size:44px}
.hero-caption .sub{font-size:36px;font-weight:400}
.hero-before{right:692px;top:246px;text-align:right}
.hero-after{left:651px;top:246px}
.hero-arrows{position:absolute;left:88px;top:474px;display:flex;gap:10px}
.hero-arrows span{width:38px;height:38px;border-radius:50%;background:rgba(255,255,255,.35);display:flex;align-items:center;justify-content:center}

/* intro */
.intro{position:absolute;left:0;top:800px;width:1200px;text-align:center}
.intro h1{font-family:"Raleway",sans-serif;font-weight:700;font-size:25px;color:var(--green-text);letter-spacing:.5px}
.intro h2{font-family:"Open Sans",sans-serif;font-weight:400;font-size:18px;color:#333;margin-top:10px}
.intro p{width:1010px;margin:18px auto 0;font-size:13px;line-height:24px;color:var(--grey-text)}

/* service cards */
.card{position:absolute;width:492px}
.card-photo{width:492px;height:277px;border:5px solid var(--white);box-shadow:0 0 6px rgba(0,0,0,.35)}
.card h3{font-family:"Raleway",sans-serif;font-weight:700;font-size:18px;color:var(--green-text);text-transform:uppercase;margin-top:30px}
.card p{font-size:12.5px;line-height:27px;color:#333;margin-top:6px;width:480px}
.btn-dark{display:inline-block;background:linear-gradient(#555,#333);color:var(--white);font-size:11.5px;text-transform:uppercase;
  padding:10px 17px;border-radius:3px;margin-top:14px;box-shadow:0 2px 3px rgba(0,0,0,.3)}

/* green band */
.feature-band{position:absolute;left:0;top:2003px;width:1200px;height:361px;background:var(--green)}
.video-frame{position:absolute;left:92px;top:37px;width:492px;height:296px;background:var(--white);padding:12px}
.video-screen{position:relative;width:100%;height:100%;background:linear-gradient(180deg,#8fa07e 0%,#6d8a55 45%,#3f8a2c 75%,#2f6e22 100%)}
.video-controls{position:absolute;left:0;bottom:0;width:100%;height:38px;background:#111}
.feature-text{position:absolute;left:612px;top:52px;width:500px;color:var(--white)}
.feature-text h3{font-family:"Raleway",sans-serif;font-weight:600;font-size:22px}
.feature-text p{font-size:12.5px;line-height:26px;margin-top:12px}
.feature-text p + p{margin-top:4px}
.btn-light{display:inline-block;background:linear-gradient(#f4f4f4,#cfcfcf);color:#333;font-size:11.5px;text-transform:uppercase;padding:11px 19px;border-radius:3px;margin-top:16px}

/* testimonial */
.testimonial{position:absolute;left:92px;top:2404px;width:560px}
.testimonial blockquote{font-family:"Raleway",sans-serif;font-weight:500;font-size:21px;line-height:33px;color:var(--green-text);text-transform:uppercase}
.testimonial p{font-size:15.5px;line-height:26px;color:#333;margin-top:20px}
.testimonial .who{font-size:12.5px;line-height:25px;color:var(--green-text);margin-top:18px}
.testimonial-photo{position:absolute;left:692px;top:2400px;width:386px;height:238px;
  background:linear-gradient(180deg,#9bb889 0%,#5aa33b 50%,#3c8a25 100%)}

/* footer */
.site-footer{position:absolute;left:0;top:2669px;width:1200px;height:270px;background:var(--light)}
.footer-links{position:absolute;left:87px;top:28px;list-style:none;font-size:13.5px;line-height:25px;color:#333}
.award-badge{position:absolute;left:330px;top:26px;width:180px;height:200px}
.quote-form{position:absolute;left:620px;top:28px;width:489px}
.quote-form h4{font-family:"Open Sans",sans-serif;font-weight:600;font-size:16.5px;line-height:31px;color:var(--green-text)}
.form-grid{display:grid;grid-template-columns:234px 234px;column-gap:21px;row-gap:11px;margin-top:18px}
.field{height:34px;background:var(--white);border:1px solid #ddd;font-size:10.5px;color:#666;padding:10px 11px}
.btn-submit{height:34px;background:linear-gradient(#3ed42c,#22a818);color:var(--white);font-size:11px;text-transform:uppercase;display:flex;align-items:center;justify-content:center}

.grass-strip{position:absolute;left:0;top:2919px;width:1200px;height:132px;
  background:linear-gradient(180deg,rgba(241,241,241,1) 0%,#8ccf5e 30%,#3a8a20 70%,#1f5a12 100%)}
.copyright{position:absolute;left:0;top:3002px;width:1200px;text-align:center;font-size:11px;color:var(--white)}
</style>
</head>
<body>

<header class="site-header">
  <div class="brand"><span class="brand-square"></span><span class="brand-name">Turf Haven</span></div>
  <div class="header-info">
    <div class="tag">Lawn specialists</div>
    <div>...from ground preparation to lawn aftercare</div>
    <div>Servicing the Auckland region</div>
    <div>0800 44 66 00</div>
  </div>
</header>

<nav class="main-nav">
  <ul>
    <li class="active">Home</li><li>About us</li><li>Services</li><li>Lawn care</li><li>Seasonal care</li><li>Hydroseeding</li><li>FAQs</li><li>Before &amp; After</li><li>Gallery</li><li>Quote / Contact</li>
  </ul>
</nav>

<section class="hero" role="img" aria-label="Garden lawn before and after grass seeding, bare soil on the left and green lawn on the right">
  <div class="hero-caption hero-before"><div class="big">BEFORE</div><div class="sub">GRASS SEEDING</div></div>
  <div class="hero-caption hero-after"><div class="big">AFTER</div><div class="sub">GRASS SEEDING</div></div>
  <div class="hero-arrows">
    <span><svg width="14" height="14" viewBox="0 0 14 14"><path d="M9 2L4 7l5 5" fill="none" stroke="#fff" stroke-width="2"/></svg></span>
    <span><svg width="14" height="14" viewBox="0 0 14 14"><path d="M5 2l5 5-5 5" fill="none" stroke="#fff" stroke-width="2"/></svg></span>
  </div>
</section>

<section class="intro">
  <h1>YOU CAN ALWAYS SPOT A TURF HAVEN LAWN</h1>
  <h2>It's the one that turns your neighbours green with envy.</h2>
  <p>If you want a lawn or playing field that looks good throughout the year, talk to us. Turf Haven are New Zealand's experts in high quality grass seeding and lawn maintenance, creating the lushest lawns you'll ever see. With high-tech equipment, years of experience and expert aftercare, nobody knows grass like Turf Haven. There are many factors that influence the quality of a lawn, including seasonality, growing conditions, shade, seed types, and time. A one-size-fits-all solution couldn't possibly guarantee a great lawn, so we provide personalised advice, a full range of seeding techniques</p>
</section>

<article class="card" style="left:92px;top:1041px">
  <div class="card-photo" role="img" aria-label="Freshly hydroseeded garden bed with blue-green mulch beside planted shrubs" style="background:linear-gradient(180deg,#4a5a3a 0%,#5b7a52 40%,#3d8a86 60%,#2e7470 100%)"></div>
  <h3>Grass seeding services</h3>
  <p>With a wide range of grass seed applications to choose from, including hydroseeding and instant lawn, there is an option to suit your property and your requirements.</p>
  <span class="btn-dark">More about grass seeding</span>
</article>

<article class="card" style="left:620px;top:1041px">
  <div class="card-photo" role="img" aria-label="Garden sprinkler spraying water across green grass" style="background:linear-gradient(180deg,#9fc86a 0%,#4f9a2a 50%,#2c6a18 100%)"></div>
  <h3>Lawn care maintenance</h3>
  <p>As well as lawn care services, the team at Turf Haven provides helpful information for regular upkeep of your residential or commercial lawn.</p>
  <span class="btn-dark">More about ongoing lawn care</span>
</article>

<article class="card" style="left:92px;top:1511px">
  <div class="card-photo" role="img" aria-label="Lush new lawn around a tree trunk beside a timber fence" style="background:linear-gradient(180deg,#bdb8a8 0%,#8a9a6a 35%,#4caa22 60%,#3a9a18 100%)"></div>
  <h3>FAQs about grass seeding and lawn care</h3>
  <p>For more information, read our frequently asked questions regarding grass seeding and lawn care.</p>
  <span class="btn-dark">Grass seeding &amp; lawn care FAQs</span>
</article>

<article class="card" style="left:620px;top:1511px">
  <div class="card-photo" role="img" aria-label="Lawn area shown half freshly seeded and half grown in front of a fence" style="background:linear-gradient(90deg,#4f8a88 0%,#4a8480 48%,#4ca52c 52%,#3f9a22 100%)"></div>
  <h3>Before and after lawn photos</h3>
  <p>See what your potential new lawn could look like by viewing a range of before and after lawn seeding photos.</p>
  <span class="btn-dark">Before and after photos</span>
</article>

<section class="feature-band">
  <div class="video-frame">
    <div class="video-screen" role="img" aria-label="Video of a finished front lawn outside a house">
      <svg class="abs" style="left:204px;top:86px" width="60" height="60" viewBox="0 0 60 60"><circle cx="30" cy="30" r="29" fill="rgba(0,0,0,.5)"/><path d="M23 17l20 13-20 13z" fill="#fff"/></svg>
      <div class="video-controls">
        <svg width="468" height="38" viewBox="0 0 468 38">
          <circle cx="20" cy="19" r="7" fill="none" stroke="#fff" stroke-width="2"/><path d="M18 15l5 4-5 4z" fill="#fff"/>
          <path d="M40 15h4l5-4v16l-5-4h-4z" fill="#fff"/>
          <rect x="58" y="17" width="40" height="4" fill="#d22"/>
          <rect x="112" y="17" width="220" height="4" fill="#555"/><rect x="112" y="17" width="60" height="4" fill="#d22"/>
          <text x="346" y="23" font-family="Open Sans,sans-serif" font-size="10" fill="#fff">01:30 / 04:55</text>
          <rect x="418" y="13" width="14" height="11" fill="none" stroke="#fff" stroke-width="1.5"/>
          <circle cx="450" cy="19" r="5" fill="none" stroke="#fff" stroke-width="2"/>
        </svg>
      </div>
    </div>
  </div>
  <div class="feature-text">
    <h3>TURF HAVEN...</h3>
    <p>For all things grass, you need the best! Turf Haven are skilled specialists when it comes to creating the perfect lawn for your property.</p>
    <p>From pre-seeding preparation to a full range of grass seeding services and lawn after care options, you'll enjoy a healthy green lawn for many years.</p>
    <p>Selling your property? Turf Haven will add the wow factor to the outdoor areas of your home with a lush green lawn.</p>
    <span class="btn-light">Find out more</span>
  </div>
</section>

<section class="testimonial">
  <blockquote>"I would recommend Turf Haven to anyone who wants an amazing lawn"</blockquote>
  <p>"Testimonial here about how great Turf Haven were to deal with and how they are so happy with the lawn and the after care services etc etc."</p>
  <div class="who">Tom Walker<br>Homeowner, Albany</div>
</section>
<div class="testimonial-photo" role="img" aria-label="Lawn mower cutting a green lawn"></div>

<footer class="site-footer">
  <ul class="footer-links">
    <li>Home</li><li>About us</li><li>Services</li><li>Lawn care</li><li>Seasonal care</li><li>Hydroseeding</li><li>FAQs</li><li>Before &amp; After Gallery</li><li>Quote / Contact</li>
  </ul>
  <svg class="award-badge" viewBox="0 0 180 200" role="img" aria-label="Horticulture qualification badge">
    <circle cx="90" cy="85" r="72" fill="#9ccc3c"/>
    <rect x="20" y="170" width="140" height="16" rx="3" fill="#6aa82a"/>
  </svg>
  <div class="quote-form">
    <h4>Get a quote for your new lawn!<br>Fill in the form or phone us on 0800 44 66 00.</h4>
    <div class="form-grid">
      <div class="field">First name</div><div class="field">Last name</div>
      <div class="field">Email address</div><div class="field">Contact phone</div>
      <div class="field">Details</div><div class="btn-submit">Call me back</div>
    </div>
  </div>
</footer>

<div class="grass-strip" role="img" aria-label="Band of grass blades along the bottom of the page"></div>
<div class="copyright">Copyright © 2015 All Rights Reserved</div>

</body>
</html>
```